Climbing Gear Company Stationary Design

We need some new stationary to standardise our business.
We require:

Business Card
A4 Letterhead
With complements slip

Our business is a Distributor and retailer of rock climbing equipment throughout Australia.
We need to the stationary (business card in particular) to reflect this.

Target Market(s)

customers, other retail outlets, overseas manufacturers.

Industry/Entity Type

Business

Requirements
Must have
• company logo
website url- www.crestwardsupply.com.au
email - marlo@crestwardsupply.com
Business Address: Unit 3, 14-16 Quarry Close, Ridgehaven, NSW, 2461
Phone: 0491 637 208
my Name (on Business card) - Marlon Pettigrew
use of Blue colour in our logo

```html
<!DOCTYPE html>
<html lang="en">
<head>
<meta charset="utf-8">
<title>Crestward Supply – Business Card</title>
<link href="https://fonts.googleapis.com/css2?family=Open+Sans:wght@400;600;700;800&display=swap" rel="stylesheet">
<style>
  :root {
    --brand-blue: #2367a3;
    --ink-grey: #5a5a5a;
    --paper: #ffffff;
    --backdrop: #ebe6df;
    --rule-grey: #b9b9b9;
  }
  * { margin: 0; padding: 0; box-sizing: border-box; }
  html, body {
    width: 1200px; height: 407px; overflow: hidden;
    background: var(--backdrop);
    font-family: "Open Sans", Arial, sans-serif;
  }
  .canvas { position: relative; width: 1200px; height: 407px; }

  .card {
    position: absolute; top: 60px;
    width: 504px; height: 288px;
  }
  .card--front { left: 60px; background: var(--paper); }
  .card--back { left: 636px; background: var(--brand-blue); color: var(--paper); }

  .wordmark {
    position: absolute; left: 0; right: 0;
    text-align: center;
    font-weight: 800; font-size: 34px; letter-spacing: 2px;
    line-height: 1;
  }
  .tagline {
    position: absolute; left: 0; right: 0;
    text-align: center;
    font-weight: 600; font-size: 14px; letter-spacing: 3.4px;
    line-height: 1;
  }
  .card--front .wordmark { top: 50px; color: var(--brand-blue); }
  .card--front .tagline { top: 92px; color: var(--brand-blue); }

  .rule {
    position: absolute; left: 0; right: 0; height: 2px;
    background: var(--brand-blue);
  }
  .rule--top { top: 131px; }
  .rule--bottom { top: 180px; }
  .name-band {
    position: absolute; left: 0; right: 0; top: 137px; height: 39px;
    background: var(--brand-blue);
    color: var(--paper);
    display: flex; align-items: center; justify-content: center;
    font-weight: 700; font-size: 16px;
  }

  .address, .contact {
    position: absolute; top: 203px;
    font-size: 12.5px; line-height: 20px; color: var(--ink-grey);
  }
  .address { right: 274px; text-align: center; }
  .contact { left: 264px; }
  .divider {
    position: absolute; left: 239px; top: 204px;
    width: 1px; height: 40px; background: var(--rule-grey);
  }
  .card--front .web {
    position: absolute; left: 0; right: 0; top: 258px;
    text-align: center; font-size: 12.5px; color: var(--ink-grey);
  }

  .card--back .wordmark { top: 106px; }
  .card--back .tagline { top: 148px; }
  .card--back .web {
    position: absolute; left: 0; right: 0; top: 256px;
    text-align: center; font-size: 13.5px; letter-spacing: 2.4px;
  }
</style>
</head>
<body>
<main class="canvas">
  <section class="card card--front" aria-label="Business card front">
    <div class="wordmark">CRESTWARD SUPPLY</div>
    <div class="tagline">THE ROPE • THE ROCK • THE JOURNEY</div>
    <div class="rule rule--top"></div>
    <div class="name-band">Marlon Pettigrew</div>
    <div class="rule rule--bottom"></div>
    <p class="address">Unit 3, 14-16 Quarry Close,<br>Ridgehaven, NSW, 2461</p>
    <div class="divider"></div>
    <p class="contact">P : 0491 637 208<br>E : marlo@crestwardsupply.com</p>
    <p class="web">www.crestwardsupply.com</p>
  </section>

  <section class="card card--back" aria-label="Business card back">
    <div class="wordmark">CRESTWARD SUPPLY</div>
    <div class="tagline">THE ROPE • THE ROCK • THE JOURNEY</div>
    <p class="web">www.crestwardsupply.com</p>
  </section>
</main>
</body>
</html>
```